Flyer for Luxury Boarding Stable for Retired Horses

A one page flyer to hand out at stable tours and at horse shows. Willow Brook at 34 Meadows is a luxury equine boarding stable for retired horses. This is a new facility in Cedar Ridge, VT that has 6 available stalls. We are trying to attract owners with 2 or more retired horses they would like to board.

Target Market(s)

Horse owners with 2 or more horses that are retired from showing, racing, or rodeo. These owners love their horses like family and want them well cared for in their retirement years.

Industry/Entity Type

Equestrian Boarding

Font styles to use
Script

Colors
EE7325
F08F49
F5BC92
FAE3D3
FDF4ED

Requirements
Must have
• Photos of the facility. Must feel upscale and worth the price.

```html
<!DOCTYPE html>
<html lang="en">
<head>
<meta charset="utf-8">
<title>Willow Brook at 34 Meadows – Retired Equine Boarding Flyer</title>
<link rel="stylesheet" href="https://fonts.googleapis.com/css2?family=Kaushan+Script&family=Poppins:wght@400;500;600;700;800&family=Yellowtail&display=swap">
<style>
  :root {
    --page-bg: #f4f4f4;
    --paper: #ffffff;
    --espresso: #2c1807;
    --wood-dark: #4a2a12;
    --wood-mid: #6b3f1d;
    --cream-line: #e9dcb4;
    --gold: #f4c64e;
    --olive-line: #5f6a34;
    --heading-brown: #3b2410;
    --green: #2f5520;
    --olive: #7c6c35;
    --amber: #c48a2e;
    --band: #b27a2f;
    --band-dark: #9a6624;
    --grey-panel: #e3e3e1;
    --text: #3a3a3a;
    --icon: #4c5a2a;
  }
  * { box-sizing: border-box; margin: 0; padding: 0; }
  html, body { width: 1200px; height: 2546px; overflow: hidden; background: var(--page-bg); }
  body { position: relative; font-family: "Poppins", sans-serif; color: var(--text); }

  .flyer {
    position: absolute; left: 40px; top: 550px;
    width: 973px; height: 1257px;
    transform: scale(1.151); transform-origin: 0 0;
    background: var(--paper); overflow: hidden;
    box-shadow: 0 6px 24px rgba(0,0,0,.18);
  }
  .abs { position: absolute; }

  .barn-photo {
    left: 0; top: 0; width: 973px; height: 480px;
    background:
      radial-gradient(ellipse 60px 80px at 50% 44%, #e9e4d2 0%, #c9b68c 50%, transparent 100%),
      linear-gradient(180deg, #7a4c22 0%, #b4843f 30%, #a77535 55%, #8d8a80 80%, #6f6a62 100%);
  }
  .wood-band {
    left: 0; top: 470px; width: 973px; height: 260px;
    background:
      repeating-linear-gradient(90deg, rgba(0,0,0,.06) 0 2px, transparent 2px 38px),
      linear-gradient(180deg, var(--wood-dark), var(--wood-mid));
  }

  .headline-plaque { left: 40px; top: 385px; width: 895px; height: 205px; }
  .headline-text { left: 0; top: 398px; width: 973px; text-align: center; }
  .kicker { color: var(--gold); font-size: 33px; font-weight: 400; line-height: 1.1; }
  .headline { color: #fff; font-weight: 800; font-size: 42px; line-height: 1.0; margin-top: 6px; letter-spacing: .3px; }
  .headline-script {
    font-family: "Yellowtail", "Kaushan Script", cursive; color: var(--gold); font-size: 86px; line-height: .9;
    margin-top: -4px; text-shadow: 2px 3px 0 var(--espresso);
  }
  .location { left: 0; top: 620px; width: 973px; text-align: center; color: #fff; font-size: 31px; font-weight: 400; }
  .location strong { font-weight: 700; }
  .location svg { vertical-align: -3px; margin-right: 6px; }

  .gallery-frame { left: 86px; top: 760px; width: 795px; height: 90px; border: 2px solid var(--olive-line); border-top: none; }
  .gallery-photo { top: 672px; width: 242px; height: 150px; border: 4px solid #a98a45; box-shadow: 0 0 0 2px #f3e9c6; }
  .photo-arena { left: 118px; background: linear-gradient(160deg, #3f7a25, #5f9a3a 45%, #cfd6c0 60%, #2f6320); }
  .photo-horse { left: 366px; background: linear-gradient(160deg, #c9d3dc, #a89480 50%, #6a4a2e 75%, #2a2a30); }
  .photo-aerial { left: 614px; background: linear-gradient(160deg, #3c6f22, #78934f 40%, #cfc6b0 65%, #3b6a26); }
  .section-title { left: 0; top: 832px; width: 973px; text-align: center; }
  .section-title span {
    background: var(--paper); padding: 0 14px; color: var(--heading-brown);
    font-weight: 700; font-size: 27px; letter-spacing: .4px;
  }

  .feature-list { top: 893px; list-style: none; }
  .feature-list li { display: flex; align-items: flex-start; gap: 10px; font-size: 13px; line-height: 15.5px; margin-bottom: 12px; color: var(--text); }
  .feature-list li span { display: block; }
  .feature-list svg { flex: 0 0 30px; }
  .features-left { left: 62px; width: 188px; }
  .features-left li span { width: 140px; }
  .features-right { left: 276px; width: 215px; }
  .features-right li span { width: 168px; }

  .stalls-pill {
    left: 66px; top: 1087px; height: 33px; padding: 0 10px 0 4px;
    background: var(--band); border-radius: 7px; color: #fff; font-size: 19px;
    display: flex; align-items: center; gap: 8px; box-shadow: 0 0 0 2px #e8d7ae inset;
  }
  .stalls-pill b { display: inline-flex; width: 26px; height: 26px; border-radius: 6px; background: var(--espresso); align-items: center; justify-content: center; font-weight: 500; }

  .fees-panel { left: 526px; top: 886px; width: 380px; height: 176px; background: var(--grey-panel); border-radius: 8px; }
  .fees-title { left: 540px; top: 893px; font-size: 23px; font-weight: 700; color: var(--heading-brown); }
  .fees-title span { color: var(--olive); }
  .fee-badge { top: 948px; width: 100px; height: 108px; text-align: center; color: #fff; }
  .fee-badge svg.shape { position: absolute; left: 0; top: 0; }
  .fee-rank {
    position: absolute; left: 34px; top: -18px; width: 32px; height: 32px; border-radius: 50%;
    background: #fff; border: 2px solid currentColor; color: var(--heading-brown);
    font-size: 14px; font-weight: 700; line-height: 28px;
  }
  .fee-rank sup { font-size: 8px; }
  .fee-label { position: absolute; left: 0; width: 100px; top: 22px; font-size: 13px; font-weight: 700; }
  .fee-amount { position: absolute; left: 0; width: 100px; top: 44px; font-size: 23px; font-weight: 700; }
  .fee-amount sup { font-size: 12px; }
  .fee-period { position: absolute; left: 0; width: 100px; top: 77px; font-size: 10px; }
  .fee-first { left: 543px; } .fee-second { left: 667px; } .fee-third { left: 788px; }

  .values-row { left: 524px; top: 1078px; display: flex; gap: 3px; }
  .value-card {
    position: relative; width: 75px; height: 58px; border: 2px solid var(--olive-line); border-radius: 7px;
    background: #fff; text-align: center; font-size: 12px; font-weight: 600; color: var(--text);
    display: flex; align-items: center; justify-content: center; line-height: 1.0; padding-top: 10px;
  }
  .value-card i {
    position: absolute; left: 50%; top: -14px; margin-left: -14px; width: 28px; height: 28px;
    border-radius: 50%; background: var(--espresso); border: 2px solid #fff;
  }

  .footer-band {
    left: 0; top: 1170px; width: 973px; height: 87px;
    background:
      repeating-linear-gradient(90deg, rgba(0,0,0,.07) 0 2px, transparent 2px 30px),
      linear-gradient(180deg, var(--band), var(--band-dark));
  }
  .contact-pill {
    left: 138px; top: 1153px; width: 697px; height: 40px; border-radius: 20px;
    background: var(--espresso); box-shadow: 0 0 0 2px #e9dcb4;
    color: #fff; font-size: 21px; font-weight: 600; text-align: center; line-height: 40px;
  }
  .call-line { left: 0; top: 1200px; width: 973px; text-align: center; color: #fbe7a8; font-size: 28px; font-weight: 600; }
  .call-line svg { vertical-align: -2px; margin: 0 4px 0 6px; }
</style>
</head>
<body>
<main class="flyer">
  <div class="abs barn-photo" role="img" aria-label="Photo of the barn aisle with wooden stalls and an open door at the far end"></div>
  <div class="abs wood-band"></div>

  <svg class="abs headline-plaque" viewBox="0 0 895 205" aria-hidden="true">
    <path d="M60 8 H835 Q855 8 858 28 Q862 48 882 52 Q892 54 892 70 V140 Q892 156 882 158 Q862 162 858 180 Q855 198 835 198 H60 Q40 198 37 180 Q33 162 13 158 Q3 156 3 140 V70 Q3 54 13 52 Q33 48 37 28 Q40 8 60 8 Z" fill="var(--espresso)" stroke="var(--cream-line)" stroke-width="4"/>
  </svg>
  <div class="abs headline-text">
    <p class="kicker">Meeting the Needs of Dedicated Horse Owners</p>
    <h1 class="headline">PROVIDING QUALITY FACILITIES &amp;<br>TREATMENT FOR</h1>
    <p class="headline-script">Retired Equines</p>
  </div>

  <p class="abs location">
    <svg width="20" height="26" viewBox="0 0 20 26"><path d="M10 1a8 8 0 0 0-8 8c0 6 8 16 8 16s8-10 8-16a8 8 0 0 0-8-8z" fill="#e23b3b"/><circle cx="10" cy="9" r="3" fill="#fff"/></svg>Located in <strong>Cedar Ridge, VT</strong>
  </p>

  <div class="abs gallery-frame"></div>
  <div class="abs gallery-photo photo-arena" role="img" aria-label="Aerial photo of the riding arena surrounded by woodland"></div>
  <div class="abs gallery-photo photo-horse" role="img" aria-label="Photo of a horse in a blanket standing in a paddock"></div>
  <div class="abs gallery-photo photo-aerial" role="img" aria-label="Aerial photo of the stable building and grounds"></div>
  <h2 class="abs section-title"><span>WILLOW BROOK AT 34 MEADOWS</span></h2>

  <ul class="abs feature-list features-left">
    <li><svg width="30" height="30" viewBox="0 0 30 30"><rect x="4" y="8" width="22" height="18" fill="none" stroke="var(--icon)" stroke-width="2"/><path d="M3 8 L15 3 L27 8" fill="none" stroke="var(--icon)" stroke-width="2"/></svg><span>Premier retirement horse boarding facility now available</span></li>
    <li><svg width="30" height="30" viewBox="0 0 30 30"><circle cx="15" cy="15" r="11" fill="none" stroke="var(--icon)" stroke-width="2"/><path d="M10 15 l4 4 l7-8" fill="none" stroke="var(--icon)" stroke-width="2"/></svg><span>Top tier amenities ensuring quality care</span></li>
    <li><svg width="30" height="30" viewBox="0 0 30 30"><rect x="4" y="6" width="22" height="20" fill="none" stroke="var(--icon)" stroke-width="2"/><path d="M4 13 H26 M15 6 V26" stroke="var(--icon)" stroke-width="2"/></svg><span>Spacious stalls with back patios</span></li>
    <li><svg width="30" height="30" viewBox="0 0 30 30"><path d="M6 26 V10 H24 V26 M6 16 H24 M10 10 V5 M20 10 V5" fill="none" stroke="var(--icon)" stroke-width="2"/></svg><span>Top-quality feed and hay provided</span></li>
  </ul>
  <ul class="abs feature-list features-right">
    <li><svg width="30" height="30" viewBox="0 0 30 30"><circle cx="10" cy="11" r="4" fill="none" stroke="var(--icon)" stroke-width="2"/><circle cx="20" cy="11" r="4" fill="none" stroke="var(--icon)" stroke-width="2"/><path d="M3 25 Q10 15 15 25 Q20 15 27 25" fill="none" stroke="var(--icon)" stroke-width="2"/></svg><span>Passionate, loving care from experienced staff</span></li>
    <li><svg width="30" height="30" viewBox="0 0 30 30"><path d="M4 12 H26 M4 20 H26 M7 6 V26 M23 6 V26" fill="none" stroke="var(--icon)" stroke-width="2"/></svg><span>Lush pastures for gentle exercise</span></li>
    <li><svg width="30" height="30" viewBox="0 0 30 30"><ellipse cx="15" cy="22" rx="11" ry="4" fill="none" stroke="var(--icon)" stroke-width="2"/><path d="M8 18 V6 M22 18 V6" stroke="var(--icon)" stroke-width="2"/></svg><span>World-class riding arena with stadium lights</span></li>
    <li><svg width="30" height="30" viewBox="0 0 30 30"><path d="M3 24 Q10 16 15 22 T27 18" fill="none" stroke="var(--icon)" stroke-width="2"/><path d="M20 14 V6 L26 8 L20 10" fill="none" stroke="var(--icon)" stroke-width="2"/></svg><span>Miles of trails through 34 meadows</span></li>
  </ul>
  <div class="abs stalls-pill"><b>6</b>AVAILABLE STALLS</div>

  <div class="abs fees-panel"></div>
  <p class="abs fees-title">BOARDING <span>FEES:</span></p>

  <div class="abs fee-badge fee-first">
    <svg class="shape" width="100" height="108" viewBox="0 0 100 108"><path d="M12 0 H88 Q100 0 100 12 V80 Q100 90 90 94 L50 108 L10 94 Q0 90 0 80 V12 Q0 0 12 0 Z" fill="var(--green)"/></svg>
    <span class="fee-rank">1<sup>ST</sup></span>
    <span class="fee-label">HORSE</span>
    <span class="fee-amount"><sup>$</sup>1,100</span>
    <span class="fee-period">PER MONTH</span>
  </div>
  <div class="abs fee-badge fee-second">
    <svg class="shape" width="100" height="108" viewBox="0 0 100 108"><path d="M12 0 H88 Q100 0 100 12 V80 Q100 90 90 94 L50 108 L10 94 Q0 90 0 80 V12 Q0 0 12 0 Z" fill="var(--olive)"/></svg>
    <span class="fee-rank">2<sup>ND</sup></span>
    <span class="fee-label">HORSE</span>
    <span class="fee-amount"><sup>$</sup>900</span>
    <span class="fee-period">PER MONTH</span>
  </div>
  <div class="abs fee-badge fee-third">
    <svg class="shape" width="100" height="108" viewBox="0 0 100 108"><path d="M12 0 H88 Q100 0 100 12 V80 Q100 90 90 94 L50 108 L10 94 Q0 90 0 80 V12 Q0 0 12 0 Z" fill="var(--amber)"/></svg>
    <span class="fee-rank">3<sup>RD</sup></span>
    <span class="fee-label">HORSE</span>
    <span class="fee-amount"><sup>$</sup>700</span>
    <span class="fee-period">PER MONTH</span>
  </div>

  <div class="abs values-row">
    <div class="value-card"><i></i>Luxurious</div>
    <div class="value-card"><i></i>Quality<br>Facilities</div>
    <div class="value-card"><i></i>Loving<br>Care</div>
    <div class="value-card"><i></i>Peaceful</div>
    <div class="value-card"><i></i>Kind</div>
  </div>

  <div class="abs footer-band"></div>
  <p class="abs contact-pill">Contact us for a tour of Willow Brook at 34 Meadows.</p>
  <p class="abs call-line">Call or text Marguerite at
    <svg width="22" height="22" viewBox="0 0 22 22"><circle cx="11" cy="11" r="10" fill="var(--green)"/><path d="M7 6 l2 0 l1 3 l-1.5 1 q1 2.5 3.5 3.5 l1-1.5 l3 1 l0 2 q-1 1.5-3 1 q-6-2-7.5-8 q-.3-2 1.5-3z" fill="#fff"/></svg>336-555-0142</p>
</main>
</body>
</html>
```